Tumbril Deli Needs a Web Page!

Tumbril Deli is a gourmet sandwich shop in Baltimore, MD USA.
We are due to open in about a month or so and we need a great web page that looks cool and is easy to use. Our Concept supports local farmers, ranchers, fishmongers & purveyors. All of our menu items are made from scratch using fresh local ingredients.

Target Market(s)

Urban people on the go & Anyone who is hungry and likes a great sandwich

Industry/Entity Type

Shop

Requirements
Must have
• We must have these 8 tabs:
Home
Menus
Gallery
About Us
Media & Events
Hours & Location
Order Online
Contact Us

Also we would like our Logo to be a focal point
Our Color scheme is Red, Black, Grey, White and a reddish-orange
however any and all colors are great and will be considered
We would love an area on the page for our own food photos to be added.
Nice to have
• Baltimore Skyline
Order Online Now Button
Free Wi-Fi Symbol
Dine-In, Take Out, Delivery,
Business Lunches, Tail Gate Platters, Catering
Should not have
• No Stock images of food or chefs.
(We want to put all of our own food photos up later.)
No Pink.

```html
<!DOCTYPE html>
<html lang="en">
<head>
<meta charset="utf-8">
<title>Tumbril Deli</title>
<link href="https://fonts.googleapis.com/css2?family=Ubuntu:wght@400;500;700&family=PT+Sans:wght@400;700&family=Open+Sans:ital,wght@0,400;0,600;1,400;1,600&family=Shadows+Into+Light&display=swap" rel="stylesheet">
<style>
:root{
  --red:#c4161c;
  --red-dark:#7a0008;
  --red-deep:#5e0006;
  --orange:#e8760f;
  --ink:#4a4a4a;
  --grey:#777;
  --light:#f1f1f1;
  --black:#1b1b1b;
  --white:#fff;
}
*{box-sizing:border-box;margin:0;padding:0}
html,body{width:1029px;height:1200px;overflow:hidden}
body{position:relative;background:var(--white);font-family:"Open Sans",sans-serif;color:var(--ink)}
.abs{position:absolute}
.top-rule{left:0;top:0;width:1029px;height:3px;background:var(--red)}
.header-band{left:0;top:3px;width:1029px;height:153px;background:linear-gradient(#fff,#e9e9e9)}
.brand{left:97px;top:15px;display:flex;align-items:center;gap:8px}
.brand-mark{width:100px;height:100px;border-radius:50%;background:var(--red);display:flex;align-items:center;justify-content:center;color:#fff;font:700 19px/1.05 "Ubuntu",sans-serif;text-align:center}
.wifi-figure{left:647px;top:34px;width:79px;height:90px;border-radius:6px;background:radial-gradient(circle at 50% 40%,#e8c3b3,#f3ece8 70%)}
.call{left:793px;top:28px;display:flex;gap:8px;align-items:center}
.call-label{font:400 13px "PT Sans",sans-serif;color:var(--red-dark)}
.call-number{font:700 16px "PT Sans",sans-serif;color:var(--red-dark)}
.sharing{left:731px;top:76px;font:400 18px "Shadows Into Light",cursive;color:#888}
.social-top{left:856px;top:84px;display:flex;gap:4px}
.social-top span{width:17px;height:17px;border-radius:3px;background:#3b7dc4}
.social-top span:last-child{background:var(--orange)}
.nav{left:87px;top:131px;width:850px;height:39px;border-radius:18px;background:linear-gradient(#e0242a,#a80c12);display:flex;overflow:hidden;box-shadow:0 0 0 2px #fff,0 1px 4px rgba(0,0,0,.3)}
.nav a{display:flex;align-items:center;justify-content:center;color:#fff;text-decoration:none;font:400 12.5px "PT Sans",sans-serif;border-left:1px solid rgba(0,0,0,.25)}
.nav a.active{background:linear-gradient(#4b4b4b,#1d1d1d);border-left:none}
.search-frame{left:94px;top:192px;width:841px;height:256px;background:#fff;box-shadow:0 0 4px rgba(0,0,0,.3)}
.search-panel{left:102px;top:200px;width:412px;height:242px;background:radial-gradient(circle at 30% 30%,#a20a14,var(--red-deep))}
.search-inner{left:111px;top:210px;width:397px;height:223px;border:1px solid #b21822}
.search-title{left:125px;top:215px;font:500 17px "Ubuntu",sans-serif;color:#fff}
.lbl{font:400 11px "PT Sans",sans-serif;color:#fff}
.field{height:18px;background:linear-gradient(#fff,#ddd);border:1px solid #999;font:italic 10px "Open Sans",sans-serif;color:#999;padding:2px 5px;display:flex;justify-content:space-between}
.field b{width:15px;height:15px;margin:-1px -4px 0 0;background:var(--red-dark);border-radius:2px}
.btn-search{left:373px;top:395px;width:81px;height:27px;border-radius:6px;background:linear-gradient(#f5953a,#d65d05);border:1px solid #fff;color:#fff;font:500 14px "Ubuntu",sans-serif;display:flex;align-items:center;justify-content:center;letter-spacing:.5px}
.hero-photo{left:517px;top:187px;width:394px;height:264px;background:radial-gradient(ellipse at 50% 60%,#e9d3a8,#b8d48a 75%)}
.hero-edge{left:911px;top:200px;width:17px;height:242px;background:linear-gradient(90deg,var(--red-dark),var(--red-deep))}
.hero-shadow{left:530px;top:452px;width:390px;height:22px;background:radial-gradient(ellipse at 50% 0,rgba(0,0,0,.22),transparent 70%)}
.card{top:484px;height:229px;border-radius:14px;background:linear-gradient(#f0f0f0,#fff 30%,#f6f6f6)}
.card h2{position:absolute;left:18px;top:12px;font:500 16px "Ubuntu",sans-serif;color:#444}
.card .thumb{position:absolute;left:12px;top:41px;right:10px;height:105px;border:1px solid #ddd;background:#fff;padding:6px}
.card .thumb div{width:100%;height:100%}
.card p{position:absolute;left:15px;right:10px;top:155px;font:400 10px/15.5px "Open Sans",sans-serif;color:#666;letter-spacing:.3px}
.card p em{font-weight:600;color:#555}
.sec-title{font:500 17px "Ubuntu",sans-serif;color:#444}
.sec-title span{color:var(--red-dark);font-weight:700}
.skyline-img{left:97px;top:802px;width:191px;height:128px;background:linear-gradient(#23428e,#3b6fb5 45%,#1a1f35 60%,#0d0f1c)}
.skyline-shadow{left:97px;top:930px;width:191px;height:14px;background:radial-gradient(ellipse at 50% 0,rgba(0,0,0,.3),transparent 70%)}
.skyline-text{left:302px;top:798px;width:340px;font:400 9px/17px "Open Sans",sans-serif;color:#666;text-align:justify}
.skyline-text em{font-weight:600;color:#555}
.divider{left:679px;top:782px;height:171px;border-left:1px dotted #999}
.dine-img{left:706px;top:816px;width:205px;height:95px;background:radial-gradient(ellipse at 50% 50%,#e8b7a6,#9ccb62 55%,#f4efe4 85%)}
.dine-shadow{left:706px;top:911px;width:205px;height:12px;background:radial-gradient(ellipse at 50% 0,rgba(0,0,0,.3),transparent 70%)}
.dine-text{left:710px;top:927px;width:225px;font:400 10px/15px "Open Sans",sans-serif;color:#666;letter-spacing:.3px}
.dine-text em{font-weight:600;color:#555}
.footer-bar{left:0;top:978px;width:1029px;height:34px;background:linear-gradient(#4a4a4a,#262626);border-bottom:1px solid #555}
.nl-label{left:111px;top:988px;font:700 11.5px "PT Sans",sans-serif;color:#fff}
.nl-input{top:986px;height:17px;background:linear-gradient(#fff,#ddd);border:1px solid #888;font:italic 9px "Open Sans",sans-serif;color:#888;padding:2px 5px}
.nl-btn{left:484px;top:986px;width:63px;height:18px;background:linear-gradient(#eee,#aaa);border:1px solid #666;border-radius:2px;font:700 10px "PT Sans",sans-serif;color:#333;display:flex;align-items:center;justify-content:center}
.legal{right:89px;top:988px;font:400 11px "PT Sans",sans-serif;color:#bbb;word-spacing:2px}
.footer{left:0;top:1012px;width:1029px;height:188px;background:#1f1f1f}
.f-title{font:700 17px "Ubuntu",sans-serif;color:#fff}
.f-title span{color:var(--orange)}
.f-dot{width:20px;height:20px;border-radius:50%;background:#cfe6f5}
.f-list{list-style:none;font:400 11px/20.6px "PT Sans",sans-serif;color:#ccc;top:1069px}
.f-list li::before{content:"";display:inline-block;width:4px;height:4px;border-radius:50%;background:var(--orange);margin:0 6px 2px 0}
.contact-intro{left:680px;top:1061px;font:400 11px/19px "PT Sans",sans-serif;color:var(--orange)}
.contact-rows{left:683px;top:1103px;font:400 11px/19px "PT Sans",sans-serif;color:#fff}
.contact-rows div{display:flex}
.contact-rows dt{width:61px}
.social-foot{left:683px;top:1173px;display:flex;gap:8px}
.social-foot span{width:26px;height:26px;border-radius:50%;background:#3f6fb0}
.social-foot span:first-child{background:var(--red)}
</style>
</head>
<body>
<div class="abs top-rule"></div>
<div class="abs header-band"></div>

<div class="abs brand"><div class="brand-mark">Tumbril<br>Deli</div></div>
<div class="abs wifi-figure" role="img" aria-label="Free Wi-Fi illustration of a person receiving signal"></div>

<div class="abs call">
  <svg width="26" height="30" viewBox="0 0 26 30"><path d="M6 2c2 0 4 5 3 7l-2 2c1 4 4 8 8 10l2-2c2-1 7 1 7 3l-1 4c-1 2-4 3-7 2C8 25 2 16 2 7 2 4 4 2 6 2z" fill="#b3101a"/></svg>
  <div><div class="call-label">Call Us Now</div><div class="call-number">(555) 318 274</div></div>
</div>
<div class="abs sharing">Sharing is caring</div>
<div class="abs social-top"><span></span><span></span><span></span><span></span></div>

<nav class="abs nav">
  <a class="active" style="width:80px">Home</a>
  <a style="width:98px">Menus</a>
  <a style="width:87px">Gallery</a>
  <a style="width:101px">About Us</a>
  <a style="width:129px">Media &amp; Events</a>
  <a style="width:138px">Hours &amp; Location</a>
  <a style="width:113px">Order Online</a>
  <a style="width:104px">Contact Us</a>
</nav>

<div class="abs search-frame"></div>
<div class="abs search-panel"></div>
<div class="abs search-inner"></div>
<div class="abs search-title">Search Your Delivery</div>
<div class="abs lbl" style="left:129px;top:252px">Dates</div>
<div class="abs field" style="left:129px;top:268px;width:103px">Start Date<b></b></div>
<div class="abs field" style="left:250px;top:268px;width:103px">End Date<b></b></div>
<div class="abs lbl" style="left:130px;top:296px">Types</div>
<div class="abs lbl" style="left:255px;top:296px">Near</div>
<div class="abs field" style="left:130px;top:313px;width:103px"><span></span><b></b></div>
<div class="abs field" style="left:251px;top:313px;width:103px"><span></span><b></b></div>
<div class="abs lbl" style="left:129px;top:340px">Keywords</div>
<div class="abs field" style="left:129px;top:360px;width:324px"></div>
<div class="abs btn-search">SEARCH</div>
<div class="abs hero-photo" role="img" aria-label="Photo of a toasted sandwich on a white plate"></div>
<div class="abs hero-edge"></div>
<div class="abs hero-shadow"></div>

<section class="abs card" style="left:88px;width:276px">
  <h2>Business Lunches</h2>
  <div class="thumb"><div role="img" aria-label="Photo of a restaurant dining room" style="background:linear-gradient(#c9a98a,#efe4d2 60%,#d8cdb8)"></div></div>
  <p><em>Lorem ipsum door sit amt, consectur adipiscing elit. Integer at lorem</em> sem. Vestibulum vulputate conectetur risus vel porta. Sed dignissim vestibu-lum enim, eget tristique dolor sodalesa.</p>
</section>
<section class="abs card" style="left:375px;width:274px">
  <h2>Tail Gate Platters</h2>
  <div class="thumb"><div role="img" aria-label="Photo of a platter of sandwiches, bread and fruit" style="background:linear-gradient(#6b3a1e,#b9783f 50%,#8a9a3a)"></div></div>
  <p><em>Lorem ipsum door sit amt, consectur adipiscing elit. Integer at lorem</em> sem. Vestibulum vulputate conectetur risus vel porta. Sed dignissim vestibu-lum enim, eget tristique dolor sodalesa.</p>
</section>
<section class="abs card" style="left:667px;width:275px">
  <h2>Catering</h2>
  <div class="thumb"><div role="img" aria-label="Photo of a catered dining room" style="background:linear-gradient(#c9a98a,#efe4d2 60%,#d8cdb8)"></div></div>
  <p><em>Lorem ipsum door sit amt, consectur adipiscing elit. Integer at lorem</em> sem. Vestibulum vulputate conectetur risus vel porta. Sed dignissim vestibu-lum enim, eget tristique dolor sodalesa.</p>
</section>

<h2 class="abs sec-title" style="left:98px;top:760px">Baltimore <span>Skyline</span></h2>
<div class="abs skyline-img" role="img" aria-label="Photo of the Baltimore skyline at night over the harbor"></div>
<div class="abs skyline-shadow"></div>
<div class="abs skyline-text">
  <p><em>Lorem Ipsum is simply dummy text of the printing and typesetting industry. Lorem Ipsum has been the industry's standard</em> dummy text ever since the 1500s, when an unknown printer took a galley of type and scrambled it to make a type specimen book. It has survived not only five centuries,</p>
  <p style="margin-top:17px"><em>But also the leap into electronic typesetting,</em> remaining essentially unchanged. It was popularised in the 1960s with the release of Letraset sheets containing Lorem Ipsum passages,</p>
</div>
<div class="abs divider"></div>
<h2 class="abs sec-title" style="left:708px;top:782px">Dine-In<span>, Take</span></h2>
<div class="abs dine-img" role="img" aria-label="Close-up photo of a ham and lettuce sandwich"></div>
<div class="abs dine-shadow"></div>
<p class="abs dine-text"><em>Lorem ipsum door sit amt, consectur adipi-scing elit. Integer at lorem</em> sem.</p>

<div class="abs footer-bar"></div>
<div class="abs nl-label">News Letter Signup</div>
<div class="abs nl-input" style="left:210px;width:129px">Your Name</div>
<div class="abs nl-input" style="left:349px;width:128px">Your Email</div>
<div class="abs nl-btn">SUBCRIBE</div>
<div class="abs legal">Blog &nbsp;| &nbsp;Contact Us &nbsp;| &nbsp;Help &nbsp;| &nbsp;Terms of Service &nbsp;| &nbsp;Support &nbsp;| &nbsp;Privacy Policy</div>

<div class="abs footer"></div>
<div class="abs f-dot" style="left:105px;top:1033px"></div>
<h3 class="abs f-title" style="left:139px;top:1030px"><span>Out,</span> Delivery</h3>
<ul class="abs f-list" style="left:103px"><li>Shipping &amp; Returns</li><li>Secure Shopping</li><li>International Shipping</li><li>Affiliates</li><li>Group Sales</li></ul>
<ul class="abs f-list" style="left:253px"><li>Shipping &amp; Returns</li><li>Secure Shopping</li><li>International Shipping</li><li>Affiliates</li><li>Group Sales</li></ul>
<ul class="abs f-list" style="left:412px"><li>Shipping &amp; Returns</li><li>Secure Shopping</li><li>International Shipping</li><li>Affiliates</li><li>Group Sales</li></ul>

<div class="abs f-dot" style="left:665px;top:1023px;background:#3fa6d6;border-radius:4px"></div>
<h3 class="abs f-title" style="left:706px;top:1021px"><span>Contact</span> info:</h3>
<p class="abs contact-intro">Lorem Ipsum is simply dummy text of the<br>printing and typesetting industry.</p>
<dl class="abs contact-rows">
  <div><dt>Phone:</dt><dd>02 5550 4172</dd></div>
  <div><dt>Mobile :</dt><dd>0400 555 318</dd></div>
  <div><dt>Office Hours :</dt><dd style="margin-left:31px">9:00am till 5:30pm</dd></div>
</dl>
<div class="abs social-foot"><span></span><span></span><span></span><span></span></div>
</body>
</html>
```